Maple Lantern Business Card

Design of business cards

Target Market(s)

We are aiming as small business owners who need anything from basic business structures, website plans, business processes and quality assurance.

Industry/Entity Type

Business

Colors

Designer to choose colors to be used in the design.

Requirements
Nice to have
• I would prefer one side of the card to use the green from the logo. Prefer to have the same font as the logo.

```html
<!DOCTYPE html>
<html lang="fr">
<head>
<meta charset="utf-8">
<title>Maple Lantern Consulting – Business Card</title>
<link href="https://fonts.googleapis.com/css2?family=Lato:wght@400;700;900&display=swap" rel="stylesheet">
<style>
  :root {
    --backdrop: #2a2a2a;
    --lime: #9cc83a;
    --lime-light: #b3d94e;
    --paper: #f4f4f4;
    --paper-shade: #e2e2e2;
    --ink: #1c1c1c;
    --slate: #4a4a4a;
    --muted: #7a7a7a;
    --rule: #8a8a8a;
  }
  * { margin: 0; padding: 0; box-sizing: border-box; }
  html, body { width: 1200px; height: 793px; overflow: hidden; }
  body {
    background: var(--backdrop);
    font-family: "Lato", Arial, sans-serif;
    display: flex;
    align-items: center;
    justify-content: center;
    gap: 40px;
  }
  .card {
    width: 540px;
    height: 309px;
    border-radius: 3px;
    position: relative;
    overflow: hidden;
  }
  /* front */
  .card-front {
    background: linear-gradient(135deg, var(--lime-light), var(--lime));
    display: flex;
    align-items: center;
    justify-content: center;
  }
  .brand {
    display: flex;
    align-items: center;
    gap: 14px;
  }
  .brand-dot {
    width: 30px; height: 30px;
    border-radius: 50%;
    flex: none;
  }
  .brand-name {
    font-weight: 700;
    font-size: 26px;
    line-height: 1.15;
    letter-spacing: 1px;
    text-transform: uppercase;
  }
  .card-front .brand-dot { background: #ffffff; }
  .card-front .brand-name { color: #ffffff; }
  /* back */
  .card-back {
    background: linear-gradient(135deg, #ffffff, var(--paper) 55%, var(--paper-shade));
    display: flex;
    padding: 28px 26px 28px 30px;
  }
  .back-brand {
    width: 230px;
    display: flex;
    align-items: center;
  }
  .card-back .brand-dot { background: var(--lime); width: 22px; height: 22px; }
  .card-back .brand-name { color: var(--lime); font-size: 21px; }
  .divider {
    width: 3px;
    align-self: stretch;
    margin: 20px 22px 0 0;
    background: linear-gradient(to bottom, transparent, var(--rule) 40%, var(--slate));
  }
  .contact { flex: 1; color: var(--ink); }
  .person-name { font-weight: 900; font-size: 15px; letter-spacing: .3px; }
  .person-role { font-size: 9.5px; color: var(--muted); letter-spacing: .6px; margin-bottom: 26px; }
  .address { font-weight: 700; font-size: 11.5px; line-height: 1.3; margin-bottom: 8px; }
  .contact-list { list-style: none; }
  .contact-list li {
    display: flex; align-items: center; gap: 10px;
    font-size: 12px; color: var(--slate); margin-bottom: 6px;
  }
  .contact-list svg { width: 13px; height: 13px; flex: none; }
  .website { font-weight: 900; font-size: 13px; margin-top: 6px; }
</style>
</head>
<body>
  <section class="card card-front">
    <div class="brand">
      <span class="brand-dot"></span>
      <span class="brand-name">Maple Lantern<br>Consulting</span>
    </div>
  </section>

  <section class="card card-back">
    <div class="back-brand">
      <div class="brand">
        <span class="brand-dot"></span>
        <span class="brand-name">Maple Lantern<br>Consulting</span>
      </div>
    </div>
    <div class="divider"></div>
    <div class="contact">
      <p class="person-name">YOUR NAME</p>
      <p class="person-role">ASSOCIÉ GÉRANT</p>
      <p class="address">12 Rue des Tilleuls,<br>93200 Valmont</p>
      <ul class="contact-list">
        <li>
          <svg viewBox="0 0 16 16" fill="#6a6a6a" aria-hidden="true"><path d="M2 5c0-2 2-3 6-3s6 1 6 3v1h-3V5H5v1H2z"/><rect x="3" y="7" width="10" height="7" rx="1"/></svg>
          +33 (0)1 40 52 18 60
        </li>
        <li>
          <svg viewBox="0 0 16 16" fill="none" stroke="#6a6a6a" stroke-width="1.5" aria-hidden="true"><rect x="4" y="1" width="8" height="14" rx="1.5"/><line x1="7" y1="12.5" x2="9" y2="12.5"/></svg>
          +33 (0)6 55 12 xx xx
        </li>
        <li>
          <svg viewBox="0 0 16 16" fill="#6a6a6a" aria-hidden="true"><rect x="4" y="1" width="8" height="4"/><rect x="1" y="6" width="14" height="6" rx="1"/><rect x="4" y="10" width="8" height="5" fill="#ffffff" stroke="#6a6a6a"/></svg>
          +33 (0)1 40 52 18 61
        </li>
        <li>
          <svg viewBox="0 0 16 16" aria-hidden="true"><rect x="1" y="3" width="14" height="10" fill="#6a6a6a"/><path d="M1 3l7 6 7-6" fill="none" stroke="#ffffff" stroke-width="1.2"/></svg>
          info@maplelantern.example
        </li>
      </ul>
      <p class="website">www.maplelantern.example</p>
    </div>
  </section>
</body>
</html>
```